Brightpath Dentistry - Flyer - Modern & Eye catching campaign flyer

Need front & back side full page flyer designs for both 1) Grand opening 2) On-going campaign.

Attached the new dental office logo.
Attached our other dental clinic flyer designs for content.

Target Market(s)

Cosmetic dentistry

Industry/Entity Type

Health Care

Requirements
Must have
• decent, modern and eye catching marketing flyers.
Nice to have
• - Nice space
• - Highlight phone number
• - Highlight special features like convenient hours, call or text, for all ages, digital facility, etc
Should not have
• - Don't want to fill the flyer with too much wordings
• - Too many colors

```html
<!DOCTYPE html>
<html lang="en">
<head>
<meta charset="utf-8">
<title>Brightpath Dentistry – Flyer</title>
<link rel="stylesheet" href="https://fonts.googleapis.com/css2?family=Source+Sans+3:wght@300;400;600;700&family=Lato:wght@400;700&display=swap">
<style>
  :root {
    --navy: #2467a6;
    --pill: #48a9c0;
    --teal: #1ba6c9;
    --ink: #2a63a0;
    --mist: #eef2f7;
    --white: #ffffff;
  }
  * { box-sizing: border-box; margin: 0; padding: 0; }
  html, body { width: 848px; height: 1200px; overflow: hidden; background: var(--white); }
  body { font-family: "Source Sans 3", sans-serif; color: var(--ink); }
  .flyer { position: relative; width: 848px; height: 1200px; overflow: hidden; background: var(--mist); }

  .hero-photo {
    position: absolute; left: 0; top: 0; width: 848px; height: 600px;
    background:
      radial-gradient(ellipse 190px 260px at 620px 170px, #d9b9a6 0%, #c8a996 35%, rgba(200,180,170,0) 70%),
      radial-gradient(ellipse 260px 320px at 760px 420px, #3e78c0 0%, rgba(62,120,192,0) 75%),
      linear-gradient(100deg, #f4f6f9 0%, #e6ecf3 40%, #9cc5dd 70%, #5b90c8 100%);
  }
  .waves { position: absolute; left: 0; top: 0; }

  .call-pill {
    position: absolute; left: 52px; top: 124px; width: 378px; height: 116px;
    background: var(--navy); border-radius: 58px;
  }
  .call-pill-inner {
    position: absolute; left: 13px; top: 14px; width: 340px; height: 88px;
    background: var(--pill); border-radius: 44px; color: var(--white);
    padding: 0 0 0 27px; box-shadow: 0 3px 6px rgba(0,0,0,.2);
  }
  .call-label { font-weight: 600; font-size: 24px; line-height: 1; padding-top: 10px; }
  .call-number { font-weight: 700; font-size: 49px; line-height: 1; letter-spacing: -0.5px; margin-top: 1px; }

  .tag-string { position: absolute; left: 228px; top: 226px; }

  .insurance-badge {
    position: absolute; left: 151px; top: 270px; width: 180px; height: 180px;
    border-radius: 50%; background: var(--white); box-shadow: 0 4px 10px rgba(0,0,0,.2);
  }
  .insurance-badge-inner {
    position: absolute; left: 15px; top: 15px; width: 150px; height: 150px; border-radius: 50%;
    background: var(--navy); color: var(--white); display: flex; align-items: center; justify-content: center;
    text-align: center; font-weight: 600; font-size: 21px; line-height: 1.3;
  }

  .headline-card {
    position: absolute; left: 430px; top: 240px; width: 279px; height: 240px;
    background: var(--white); border-radius: 28px 28px 0 0;
  }
  .headline-panel {
    position: absolute; left: 444px; top: 254px; width: 251px; height: 210px;
    background: var(--navy); border-radius: 22px 22px 0 0; color: var(--white); text-align: center;
    padding-top: 10px;
  }
  .headline-small { font-weight: 600; font-size: 27px; line-height: 1; }
  .headline-big { font-weight: 700; font-size: 52px; line-height: 0.95; letter-spacing: 0.5px; }
  .headline-small.last { margin-top: 6px; }

  .about-box {
    position: absolute; left: 430px; top: 398px; width: 279px; height: 486px;
    border: 2px dotted var(--navy); border-top: none; border-radius: 0 0 34px 34px;
  }
  .about-text {
    position: absolute; left: 455px; top: 462px; width: 250px;
    font-weight: 300; font-size: 24.5px; line-height: 40px; color: var(--ink);
  }
  .about-text strong { font-weight: 700; }

  .services-pill {
    position: absolute; left: 102px; top: 469px; width: 295px; height: 87px;
    background: var(--pill); border-radius: 38px; color: var(--white); text-align: center;
    font-weight: 700; font-size: 27px; line-height: 28px; padding-top: 15px;
  }
  .features { position: absolute; left: 98px; top: 572px; width: 300px; text-align: center; list-style: none; }
  .features li { font-weight: 600; font-size: 19.5px; line-height: 24px; }
  .features li + li { margin-top: 32px; }
  .features li:nth-child(3), .features li:nth-child(4) { margin-top: 14px; }

  .find-us {
    position: absolute; left: 36px; top: 892px; width: 403px; height: 278px;
    background: var(--navy); border-radius: 34px; box-shadow: 0 5px 10px rgba(0,0,0,.25);
  }
  .find-us-title { position: absolute; left: 41px; top: 12px; color: var(--white); font-weight: 700; font-size: 30px; }
  .map-frame {
    position: absolute; left: 11px; top: 47px; width: 380px; height: 218px;
    background: var(--white); border-radius: 22px;
  }
  .map-area {
    position: absolute; left: 7px; top: 7px; width: 366px; height: 204px;
    background: linear-gradient(135deg, #ececec 0%, #e4e4e4 50%, #eaeaea 100%);
  }

  .brand { position: absolute; left: 470px; top: 925px; display: flex; align-items: center; gap: 12px; }
  .brand-dot { width: 46px; height: 46px; border-radius: 50%; background: var(--pill); }
  .brand-name { font-family: "Lato", sans-serif; font-weight: 700; font-size: 31px; color: var(--pill); line-height: 1.05; }

  .contacts { position: absolute; left: 462px; top: 1076px; list-style: none; }
  .contacts li { display: flex; align-items: center; height: 34px; font-family: "Lato", sans-serif; font-weight: 700; font-size: 23px; color: var(--pill); letter-spacing: 0.4px; }
  .contacts svg { margin-right: 12px; flex: none; }
</style>
</head>
<body>
<main class="flyer">
  <div class="hero-photo" role="img" aria-label="Photo of a smiling dental professional in blue scrubs with a mask lowered under her chin, in a bright clinic"></div>

  <svg class="waves" width="848" height="1200" viewBox="0 0 848 1200" aria-hidden="true">
    <path d="M0,432 Q420,330 848,575 L848,1200 L0,1200 Z" fill="#eef2f7"/>
    <path d="M0,415 Q420,318 848,555 L848,575 Q420,340 0,432 Z" fill="#1ba6c9"/>
    <path d="M0,935 C220,1060 520,1078 848,1028 L848,1200 L0,1200 Z" fill="#ffffff"/>
    <path d="M0,935 C220,1060 520,1078 848,1028 L848,1034 C520,1092 220,1082 0,1000 Z" fill="#1ba6c9"/>
  </svg>

  <section class="call-pill">
    <div class="call-pill-inner">
      <p class="call-label">Call or Text Us Now:</p>
      <p class="call-number">484.555.0172</p>
    </div>
  </section>

  <svg class="tag-string" width="28" height="72" viewBox="0 0 28 72" aria-hidden="true">
    <ellipse cx="14" cy="36" rx="9" ry="32" fill="none" stroke="#1a2a3a" stroke-width="1.5"/>
    <circle cx="14" cy="4" r="3.5" fill="#ffffff"/>
    <circle cx="14" cy="68" r="3.5" fill="#ffffff"/>
  </svg>

  <div class="insurance-badge">
    <div class="insurance-badge-inner">ALL<br>INSURANCES<br>ACCEPTED</div>
  </div>

  <div class="headline-card"></div>
  <section class="headline-panel">
    <p class="headline-small">LOOKING FOR</p>
    <p class="headline-big">DENTIST</p>
    <p class="headline-small last">CLOSE TO HOME?</p>
  </section>

  <div class="about-box"></div>
  <p class="about-text">Come and See Us<br>for Professional<br>Services and Care.<br>Our dentists and<br>staff are experts in<br>the field of<br>advanced dentistry<br>and will help you<br>achieve<br><strong>your perfect smile.</strong></p>

  <h2 class="services-pill">FAMILY &amp; COSMETIC<br>DENTISTRY</h2>
  <ul class="features">
    <li>State-Of-The-Art equipment<br>and paperless facility.</li>
    <li>Filled with entertainment<br>devices for patient comfort.</li>
    <li>Same-day appointment for<br>Dental Emergencies</li>
    <li>Helping community with<br>routine free kids dental<br>screening.</li>
  </ul>

  <section class="find-us">
    <h2 class="find-us-title">FIND US</h2>
    <div class="map-frame">
      <div class="map-area" role="img" aria-label="Street map showing the clinic location and surrounding roads"></div>
    </div>
  </section>

  <div class="brand">
    <span class="brand-dot"></span>
    <span class="brand-name">Brightpath<br>Dentistry</span>
  </div>

  <ul class="contacts">
    <li>
      <svg width="30" height="30" viewBox="0 0 30 30" aria-hidden="true"><circle cx="15" cy="15" r="14" fill="#1ba6c9"/><circle cx="15" cy="15" r="8" fill="none" stroke="#fff" stroke-width="1.8"/><ellipse cx="15" cy="15" rx="3.5" ry="8" fill="none" stroke="#fff" stroke-width="1.5"/><line x1="7" y1="15" x2="23" y2="15" stroke="#fff" stroke-width="1.5"/></svg>
      www.BrightpathSmile.com
    </li>
    <li>
      <svg width="30" height="30" viewBox="0 0 30 30" aria-hidden="true"><circle cx="15" cy="15" r="14" fill="#1ba6c9"/><rect x="7.5" y="7.5" width="15" height="15" rx="3" fill="#fff"/><path d="M11,10.5 l2,0 l1,3 l-1.3,1 q1.3,2.4 3.3,3.3 l1,-1.3 l3,1 l0,2 q-0.5,1 -1.6,1 q-7.5,-1.2 -8.4,-8.4 q0,-1.1 1,-1.6 z" fill="#1ba6c9"/></svg>
      info@BrightpathSmile.com
    </li>
    <li>
      <svg width="30" height="30" viewBox="0 0 30 30" aria-hidden="true"><circle cx="15" cy="15" r="14" fill="#1ba6c9"/><rect x="7.5" y="9.5" width="15" height="11" rx="2" fill="#fff"/><path d="M8.5,10.5 L15,15.5 L21.5,10.5" fill="none" stroke="#1ba6c9" stroke-width="1.5"/></svg>
      484-555-0172
    </li>
  </ul>
</main>
</body>
</html>
```